Commercial Broker Profile Flyer

I need a one-page flyer created that will serve as a profile report for individual brokers within a commercial real estate firm. The flyer will include company branding, agent photo, bio, and other information. I would like to have the source file available for future editing preferably in a Publisher file format. A copy of a company brochure is included and would like to have this profile flyer similar to keep company branding consistent. Our company website is www.coltbrinwellre.com for any other questions on branding.

Target Market(s)

Professional

Industry/Entity Type

Real Estate Agent

Requirements
Must have
• One page
• Source files MUST include a .PUB file that I can update in the future
• All of the information in the uploaded "content" file
• Company branding
• Must be 8.5"x11"
Should not have
• Do not use stock photos or property photos from the attachments. I only want the broker photo and company logo.

```html
<!DOCTYPE html>
<html lang="en">
<head>
<meta charset="utf-8">
<title>Broker Profile – Colt-Brinwell Real Estate</title>
<link href="https://fonts.googleapis.com/css2?family=Catamaran:wght@400;600;700&display=swap" rel="stylesheet">
<style>
  :root{
    --green:#0b6a3b;
    --green-head:#0e6b36;
    --maroon:#230a10;
    --white:#ffffff;
    --ink:#222222;
    --photo-light:#b9bcb9;
    --photo-dark:#7d807d;
    --stage:#1e1e1e;
  }
  *{box-sizing:border-box;margin:0;padding:0}
  html,body{width:1200px;height:960px;overflow:hidden;background:var(--stage)}
  body{font-family:"Catamaran",sans-serif;position:relative}
  .flyer{
    position:absolute;left:229px;top:0;width:894px;height:1158px;
    transform:scale(.829);transform-origin:0 0;background:var(--white);overflow:hidden;
  }
  .broker-photo{
    position:absolute;left:0;top:100px;width:340px;height:482px;
    background:radial-gradient(circle at 50% 45%,var(--photo-light),var(--photo-dark));
  }
  .bio-panel{position:absolute;left:344px;top:100px;width:550px;height:482px;background:var(--maroon);color:var(--white)}
  .bio-panel h2{position:absolute;left:26px;top:102px;font-size:22px;font-weight:700}
  .bio-text{position:absolute;left:26px;top:146px;width:498px;font-size:16px;line-height:19.3px;text-align:justify}
  .bio-text p+p{margin-top:19.3px}
  .header-wave{position:absolute;left:0;top:0;width:894px;height:190px}
  .brand{position:absolute;left:54px;top:58px;display:flex;align-items:center;gap:16px;color:var(--white)}
  .brand-mark{width:86px;height:86px;border-radius:50%;background:var(--white)}
  .brand-name{font-weight:400;line-height:1}
  .brand-name .firm{display:block;font-size:48px}
  .brand-name .kind{display:block;font-size:21px;letter-spacing:7px;margin-top:4px;padding-left:30px}
  .section-title{color:var(--green-head);font-weight:700;text-decoration:underline;text-underline-offset:3px;position:absolute}
  .clients-title{left:47px;top:592px;font-size:24px}
  .clients{position:absolute;left:52px;top:632px;list-style:none;font-size:18px;color:var(--ink)}
  .clients li{height:35px;line-height:35px}
  .clients li::before{content:"• ";font-size:14px}
  .affil-title{left:391px;top:652px;font-size:26px}
  .affiliations{position:absolute;left:412px;top:692px;list-style:none;font-size:20px;color:var(--ink);line-height:25px}
  .affiliations li{position:relative;padding-left:21px;margin-bottom:10px}
  .affiliations li::before{content:"•";position:absolute;left:0;font-size:14px}
  .footer-wave{position:absolute;left:0;top:900px;width:894px;height:258px}
  .contact{position:absolute;color:var(--white);text-align:center;line-height:1.2}
  .contact-office{left:98px;top:1000px;width:240px}
  .contact-office .label{font-size:15px;font-weight:600;display:block;margin-bottom:20px}
  .contact-office .name{font-size:18px;font-weight:700;display:block}
  .contact-office .role{font-size:15px;font-weight:600;display:block;margin-bottom:16px}
  .contact-office .small{font-size:14px;font-weight:600;display:block}
  .contact-office .big{font-size:18px;font-weight:700;display:block}
  .contact-direct{left:540px;top:1058px;width:340px}
  .contact-direct div{height:29px}
  .contact-direct .small{font-size:14px;font-weight:600}
  .contact-direct .big{font-size:18px;font-weight:700}
</style>
</head>
<body>
<main class="flyer">
  <div class="broker-photo" role="img" aria-label="Broker headshot portrait on a grey studio backdrop"></div>

  <section class="bio-panel">
    <h2>Bio</h2>
    <div class="bio-text">
      <p>Reed began his real estate career in 2005 and has completed $75+ million in transactions representing sellers and buyers of commercial real estate, providing tenant representation, and leasing of retail and office properties. Prior to beginning his real estate career, Reed served over five years in the Army Reserves and attended Piedmont State University.</p>
      <p>Reed has earned the prestigious Certified Commercial Realty Advisor (CCRA) designation as well as the Certified Leasing Professional (CLP) designation. Reed is a member of the Retail Property Council (RPC), the Carolina and Harbor City Broker Association, the Harbor City-Ridge County Chamber of Commerce, and serves on the board of directors for the NC-CCRA Chapter, the Sandhill Community Youth Center, and the Tall Pines Brokers Association. Reed is a licensed real estate broker in NC and SC.</p>
    </div>
  </section>

  <svg class="header-wave" viewBox="0 0 894 190" aria-hidden="true">
    <path d="M0,0 H894 V112 H650 C480,112 330,178 170,176 C95,175 35,162 0,150 Z" fill="var(--green)"/>
    <path d="M894,114 H650 C480,114 330,180 170,178 C95,177 35,164 0,152" fill="none" stroke="var(--white)" stroke-width="6"/>
  </svg>

  <div class="brand">
    <span class="brand-mark"></span>
    <span class="brand-name"><span class="firm">Colt-Brinwell</span><span class="kind">REAL ESTATE</span></span>
  </div>

  <h3 class="section-title clients-title">Clients Served</h3>
  <ul class="clients">
    <li>Cluckworth's</li><li>Six Griddles</li><li>Game Day Cuts</li><li>Tread Depot</li><li>Tiny Crumbs</li>
    <li>Bridgeway Home Health</li><li>Kinfolk Ventures</li><li>Hometown Reach</li><li>Fizzline Bottling Co.</li>
  </ul>

  <h3 class="section-title affil-title">Professional Affiliations</h3>
  <ul class="affiliations">
    <li>Certified Commercial Realty<br>Advisor (designee)</li>
    <li>Retail Property Council</li>
    <li>Tall Pines Brokers Association</li>
    <li>Carolina Brokers Commercial Forms Committee</li>
  </ul>

  <svg class="footer-wave" viewBox="0 0 894 258" aria-hidden="true">
    <circle cx="710" cy="120" r="140" fill="var(--green)" opacity=".08"/>
    <path d="M0,122 C120,88 260,68 420,92 C570,116 720,136 894,136 V258 H0 Z" fill="var(--maroon)"/>
    <path d="M0,138 C120,106 260,86 420,110 C570,134 720,149 894,149 V258 H0 Z" fill="var(--green)"/>
  </svg>

  <div class="contact contact-office">
    <span class="label">Contact Information</span>
    <span class="name">T. Reed Brinwell, CCRA, CLP</span>
    <span class="role">Principal / Broker in Charge</span>
    <span class="small">Office Phone:</span>
    <span class="big">(910) 555-0172 ext. 202</span>
  </div>

  <div class="contact contact-direct">
    <div><span class="small">Cell Phone: </span><span class="big">(910) 555-0148</span></div>
    <div><span class="small">Email: </span><span class="big">reed@coltbrinwellre.com</span></div>
    <div><span class="small">Website: </span><span class="big">www.coltbrinwellre.com</span></div>
  </div>
</main>
</body>
</html>
```